Plinthmoor Assessments Landing Page

We need a landing page re-designed for a new website www.plinthmoorassessments.example and the website is live if you search the address provided.
We need the industry standard files for embedding this into the landing page of our website. The company is a real estate advisory firm, we provide professional property services and are focused on business rates (commercial property taxation in the UK).
We have uploaded a file which is meant to provide a visual guide as to how we envisage the landing page looking. You are free to come up with an entirely different creative design. The image at the top with the search button is taken from another website so the design will need to be distinctly different but may follow the same theme. Furthermore, the colour palette does not need to be followed slavishly and can be modified changed and improved upon. It might be that you want to incorporate other visual cues such as a desktop PC, laptop and iPad as these are devices the website will be accessed from; however, this is not essential and only a guide.
**To clarify, please note, the target industry is commercial properties and not residential or domestic property, so please when incorporating designs of buildings its important to focus on commercial property such as shops, offices, industrial buildings etc.**
Target Market(s)
Occupiers of commercial real estate in the UK who pay property tax to occupy the property.
Look and feel
Each slider illustrates characteristics of the customer's brand and the style your logo design should communicate.

```html
<!DOCTYPE html>
<html lang="en">
<head>
<meta charset="utf-8">
<title>Plinthmoor Assessments</title>
<link rel="stylesheet" href="https://fonts.googleapis.com/css2?family=Montserrat:wght@300;400;500;600;700;800&family=Open+Sans:ital,wght@0,400;0,600;0,700;1,400&display=swap">
<style>
:root{
  --orange:#e64a1e;
  --orange-bright:#f58634;
  --orange-button:#f47b20;
  --ink:#1a1a1a;
  --text:#444444;
  --muted:#555555;
  --pale:#eeeef0;
  --line:#e4e4e4;
  --charcoal:#262626;
  --white:#ffffff;
  --black:#0d0d0d;
}
*{margin:0;padding:0;box-sizing:border-box}
html,body{width:734px;height:1200px;overflow:hidden;background:var(--white)}
body{position:relative;font-family:"Open Sans",sans-serif;color:var(--text)}
.abs{position:absolute}

/* top strip */
.top-strip{left:0;top:0;width:734px;height:10px;background:var(--orange)}
.account-tab{left:485px;top:0;width:143px;height:10px;background:var(--black);display:flex;justify-content:space-around;align-items:center;font-family:"Montserrat",sans-serif;font-size:4.6px;color:var(--white);letter-spacing:.2px}

/* header */
.brand{display:flex;align-items:center;gap:4px;font-family:"Montserrat",sans-serif;font-weight:600;color:var(--ink);text-transform:uppercase;line-height:1}
.brand-mark{background:var(--orange);flex:none}
.brand-header{left:106px;top:13px}
.brand-header .brand-mark{width:14px;height:14px}
.brand-header .brand-name{font-size:6.4px;letter-spacing:.1px}
.main-nav{left:195px;top:19px;display:flex;gap:8px;font-family:"Montserrat",sans-serif;font-size:5.3px;letter-spacing:.5px;color:var(--ink)}
.contact-btn{left:481px;top:16px;width:53px;height:12px;background:var(--black);border-radius:2px;color:var(--white);font-family:"Montserrat",sans-serif;font-weight:700;font-size:4.8px;display:flex;align-items:center;justify-content:center}
.social-dots{display:flex;align-items:center}
.social-dots span{border-radius:50%;background:var(--ink);display:block}
.social-header{left:543px;top:19px;gap:8px}
.social-header span{width:5px;height:5px}
.accreditation{left:600px;top:15px;width:26px;height:14px;border-radius:3px;background:var(--ink)}

/* hero: split panel */
.hero{left:0;top:34px;width:734px;height:256px;background:var(--charcoal)}
.hero-accent{left:0;top:286px;width:734px;height:4px;background:var(--orange)}
.hero-title{left:106px;top:62px;width:330px;font-family:"Montserrat",sans-serif;font-weight:800;font-size:16px;line-height:20px;color:var(--orange-bright);text-transform:uppercase}
.hero-sub{left:106px;top:112px;width:330px;font-family:"Montserrat",sans-serif;font-weight:700;font-size:10px;line-height:13px;color:var(--white)}
.hero-fee{left:106px;top:150px;width:289px;height:18px;background:var(--white);font-family:"Montserrat",sans-serif;font-size:10px;color:var(--ink);display:flex;align-items:center;padding-left:9px}
.search-field{left:106px;top:192px;width:330px;height:30px;background:var(--white);border-radius:15px;border:2px solid var(--orange)}
.search-placeholder{left:118px;top:202.5px;width:200px;font-size:6.2px;color:var(--muted);white-space:nowrap;overflow:hidden;text-overflow:ellipsis}
.search-btn{left:330px;top:196px;width:102px;height:22px;background:var(--orange-button);border-radius:11px;color:var(--white);font-size:6.8px;display:flex;align-items:center;justify-content:center;gap:4px}
.hero-photo{left:466px;top:52px;width:162px;height:216px;border-radius:4px;background:linear-gradient(160deg,#9a9a9a 0%,#6e6e6e 55%,#3e3e3e 100%)}

/* understanding */
.section-title{left:0;top:312px;width:734px;text-align:center;font-family:"Montserrat",sans-serif;font-weight:400;font-size:15.6px;color:var(--ink)}
.card{top:355px;width:149px;height:245px;background:var(--white);border:1px solid var(--line);border-bottom:4px solid var(--orange)}
.card-photo{width:147px;height:56px;display:block}
.card-text{font-style:italic;font-size:7px;line-height:11.2px;color:var(--text);text-align:center;padding:0 7px;margin-top:12px}

/* coverage */
.coverage{left:0;top:630px;width:734px;height:181px;background:linear-gradient(180deg,#e8521f 0%,#e44a1b 60%,#d9461a 100%)}
.coverage-title{left:0;top:667px;width:734px;text-align:center;font-family:"Montserrat",sans-serif;font-weight:300;font-size:15.4px;color:var(--white)}
.coverage-text{left:136px;top:707px;width:462px;text-align:center;font-size:8.4px;line-height:15.6px;color:var(--white)}

/* fees */
.fees-pale{left:0;top:811px;width:339px;height:217.5px;background:var(--pale)}
.fees-photo{left:339px;top:811px;width:395px;height:217.5px;background:linear-gradient(135deg,#3a3a3a 0%,#8a8a8a 45%,#d6d6d6 70%,#5a5a5a 100%)}
.fees-card{left:106px;top:822.5px;width:369.5px;height:176.5px;background:var(--white);padding:22px 15px 0 15.7px}
.fees-title{font-family:"Montserrat",sans-serif;font-weight:400;font-size:16px;color:var(--ink);margin-bottom:11px;white-space:nowrap}
.fees-body{font-size:7.4px;line-height:11.2px;color:var(--muted)}
.fees-strong{font-size:7.4px;line-height:11.2px;font-weight:600;color:var(--ink);margin-top:11px}

/* call to action */
.cta-band{left:0;top:1028.5px;width:734px;height:55.5px;background:var(--orange)}
.cta-text{left:106px;top:1050px;font-family:"Montserrat",sans-serif;font-weight:700;font-size:9.2px;color:#fde8dc;letter-spacing:.1px}
.cta-btn{left:500px;top:1044px;width:128px;height:24.5px;background:var(--black);border-radius:3px;color:var(--white);font-family:"Montserrat",sans-serif;font-size:9.8px;display:flex;align-items:center;justify-content:center}

/* footer */
.brand-footer{left:108px;top:1092px;gap:6px}
.brand-footer .brand-mark{width:24px;height:24px}
.brand-footer .brand-name{font-size:10.4px;line-height:12px}
.footer-nav{top:1100.5px;font-weight:700;font-size:6.4px;color:var(--ink);letter-spacing:.1px}
.company-info{left:105px;top:1134.5px;font-size:5.9px;line-height:11px;color:var(--text)}
.company-info b{font-weight:700;color:var(--ink)}
.follow{left:492px;top:1145.5px;font-weight:700;font-size:6.1px;color:var(--ink)}
.social-footer{left:541px;top:1144px;gap:14px}
.social-footer span{width:9px;height:9px}
.legal-bar{left:0;top:1171px;width:734px;height:29px;background:var(--black);color:var(--white);font-family:"Montserrat",sans-serif;font-weight:700;font-size:6px;letter-spacing:1.2px;display:flex;align-items:center;justify-content:center}
</style>
</head>
<body>

<div class="abs top-strip"></div>
<div class="abs account-tab"><span>LOGIN</span><span>REGISTER</span><span>BOOK VALUATION NOW</span></div>

<header>
  <div class="abs brand brand-header"><span class="brand-mark"></span><span class="brand-name">Plinthmoor<br>Assessments</span></div>
  <nav class="abs main-nav"><span>PROPERTY SEARCH</span><span>DISCOVER</span><span>ABOUT</span></nav>
  <div class="abs contact-btn">CONTACT US</div>
  <div class="abs social-dots social-header" aria-label="Social links"><span></span><span></span><span></span></div>
  <div class="abs accreditation" role="img" aria-label="Professional accreditation badge"></div>
</header>

<section>
  <div class="abs hero"></div>
  <div class="abs hero-accent"></div>
  <div class="abs hero-photo" role="img" aria-label="Black and white photo of a high street with shop fronts and offices"></div>
  <h1 class="abs hero-title">Do you think your business rates are too high?</h1>
  <p class="abs hero-sub">Use our free valuation tool below or book a valuation with one of our qualified surveyors.</p>
  <div class="abs hero-fee">No shock commissions and fair fixed fees from £295!</div>
  <div class="abs search-field"></div>
  <div class="abs search-placeholder">Enter your commercial property postcode to begin the evaluation process..</div>
  <div class="abs search-btn">
    <svg width="7" height="7" viewBox="0 0 10 10"><circle cx="4" cy="4" r="3" fill="none" stroke="#fff" stroke-width="1.5"/><path d="M6.3 6.3L9 9" stroke="#fff" stroke-width="1.6"/></svg>
    <span>Start free valuation now</span>
  </div>
</section>

<section>
  <h2 class="abs section-title">A Better Understanding of your Rates Payments</h2>

  <article class="abs card" style="left:129.5px">
    <div class="card-photo" role="img" aria-label="Photo of a smiling woman beside a network of connected profile portraits" style="background:linear-gradient(90deg,#e8c3a8 0%,#f4f4f4 45%,#d8d8d8 100%)"></div>
    <p class="card-text">We pride ourselves on working collaboratively with our clients. That’s why we offer a free online valuation tool which will help you better understand your rateable valuation and rates payable. We advise checking the factual data shown on the Summary Valuation Breakdown with what is actually on the ground at your property, measuring it at all floor levels noting the size and any other property features.</p>
  </article>

  <article class="abs card" style="left:292.5px">
    <div class="card-photo" role="img" aria-label="Photo of hands holding a tablet showing a property website" style="background:linear-gradient(90deg,#e9d6c2 0%,#c9a88a 50%,#7a6a60 100%)"></div>
    <p class="card-text">Use our free valuation tool to estimate the rateable value of your commercial property in England and Wales. You can add, remove or alter the property information, make allowances and set the base rate pricing. At the end we will provide an estimate of the amount of rates payable and any potential savings.</p>
  </article>

  <article class="abs card" style="left:455.5px">
    <div class="card-photo" role="img" aria-label="Photo of a hand holding a mobile phone above a laptop keyboard" style="background:linear-gradient(120deg,#c97a5a 0%,#b48a76 40%,#8c8c96 75%,#6e6e7a 100%)"></div>
    <p class="card-text">Need help? Book a qualified surveyor to advise you on the rateable value of your commercial property. You can book an essential desktop based valuation or a detailed on-site valuation.<br>Our surveyors are not driven by high commissions and will give you an honest fair assessment of your rateable valuation, rates payable and advise you on whether you should commence the Check, Challenge and Appeal process.</p>
  </article>
</section>

<section>
  <div class="abs coverage" role="img" aria-label="Orange toned photo of city office tower blocks"></div>
  <h2 class="abs coverage-title">We got you covered</h2>
  <p class="abs coverage-text">Our rating list contains the most up-to-date information of around 2 million commercial properties in England and Wales. Our qualified rating surveyors provide nationwide coverage and we employ some of the highest qualified surveyors with some holding Chartered Rating Diploma.</p>
</section>

<section>
  <div class="abs fees-pale"></div>
  <div class="abs fees-photo" role="img" aria-label="Black and white photo of a business handshake over a desk with a laptop and contract papers"></div>
  <div class="abs fees-card">
    <h2 class="fees-title">Fair fixed fees and no shock commissions!</h2>
    <p class="fees-body">Our fees are fixed up front, ensuring there are no surprises and we promise to never charge any shock commisions. Not only does this provide you with certainty of cost, it also provides you with confidence that our surveyors are not lead by the prospect of large commission payments. We are here from initial point of contact right through to the end, be that to provied an essential desktop valuation, on-site valuation or helping you through the Check, Challenge and Appeal process. We're here to support and guide you every step of the way.</p>
    <p class="fees-strong">Our surveyors don't do speculative appeals, we provied honest and professional advice at a fair fixed fee.</p>
  </div>
</section>

<section>
  <div class="abs cta-band"></div>
  <p class="abs cta-text">BOOK A RATEABLE VALUATION WITH ONE OF OUR QUALIFIED SURVEYORS</p>
  <div class="abs cta-btn">Book Valuation Now</div>
</section>

<footer>
  <div class="abs brand brand-footer"><span class="brand-mark"></span><span class="brand-name">Plinthmoor<br>Assessments</span></div>
  <span class="abs footer-nav" style="left:419.5px">PRICING PLANS</span>
  <span class="abs footer-nav" style="left:486px">FAQS</span>
  <span class="abs footer-nav" style="left:526px">CONTACT</span>
  <span class="abs footer-nav" style="left:579.5px">LEGAL &amp; TERMS</span>
  <p class="abs company-info"><b>COMPANY REGISTRATION NUMBER</b>: 10457312<br><b>COMPANY REGISTERED ADDRESS:</b> Harrow House, Quayside Park, Manchester M50 9ZZ</p>
  <span class="abs follow">FOLLOW US:</span>
  <div class="abs social-dots social-footer" aria-label="Social links"><span></span><span></span><span></span></div>
  <div class="abs legal-bar">© 2019 ALL RIGHTS RESERVED.</div>
</footer>

</body>
</html>
```